Website Design for a High School

School Name: Bayt Qamarin Private Schools
sub-schools:
1-Bayt Qamarin Primary School
2-Bayt Qamarin High School for Girls
3-Bayt Qamarin High School for Boys
The design should be professional and serious and below is the details of the website.
Pages: (Home, About Us, Schools, Events, Students, Gallery, Lectures, Contact Us).
A-) Home Page:
1-Animated photos banner as main
2-Marquee for the last news.
3-Welcoming block of text
4-latest news at the body of the page.
5-Calender "on the side"
6-Number of visitors "on the side"
7-Search bar
8-options to choose a school
B-) School Page:
three schools listed as drop down menu when highlighted over the Schools button in the menu
*Each school page should contain:
1-Student login area
2-Animation photos header
3-Specific news and projects
C-) Student Login page:
have a Report Card
D-) Gallery Page
have a collection of photos.
E-)Contact Page
phone numbers
emails
feedback form
F-)Other mentioned pages
with normal text and photos page look as similar to the Home page.
Required color: Purple as main and include the logo colors
Logo: is attached.
Button link to change language to Arabic.

```html
<!DOCTYPE html>
<html lang="en">
<head>
<meta charset="utf-8">
<title>Bayt Qamarin Private Schools</title>
<link href="https://fonts.googleapis.com/css2?family=Roboto+Condensed:wght@400;700&family=Raleway:wght@400;600&display=swap" rel="stylesheet">
<style>
:root{
  --purple:#6d44a5;
  --purple-deep:#5c3592;
  --purple-soft:#8f62c0;
  --ink:#333;
  --muted:#777;
  --light:#ebebeb;
  --card:#e4e4e4;
  --navy:#2c3e50;
  --gold:#f0a21e;
  --footer:#2b2b2b;
}
*{margin:0;padding:0;box-sizing:border-box}
html,body{width:843px;height:1200px;overflow:hidden;background:#fff}
body{font-family:"Raleway",sans-serif;color:var(--ink);position:relative}
.abs{position:absolute}

/* top bar */
.topbar{left:0;top:0;width:843px;height:49px;border-top:2px solid var(--purple);background:#fff}
.visits{left:478px;top:19px;font-size:8px;font-weight:600;display:flex;align-items:center;gap:5px;color:var(--ink)}
.visits .dot{width:12px;height:12px;border-radius:50%;background:var(--purple)}
.visits b{color:var(--purple)}
.lang{left:600px;top:19px;font-size:8px;display:flex;gap:10px;font-weight:600}
.lang span:first-child{color:#aaa;text-decoration:underline}
.lang span:last-child{color:var(--ink);border-bottom:1px solid var(--ink)}
.social{left:682px;top:20px;display:flex;gap:10px}
.social i{display:block;width:9px;height:9px;border-radius:50%;background:#999}

/* nav */
.nav{left:0;top:49px;width:843px;height:45px;background:var(--purple)}
.nav ul{list-style:none}
.nav li{position:absolute;top:17px;font-family:"Roboto Condensed",sans-serif;font-size:8px;line-height:10px;color:#f0eaf7;letter-spacing:.2px;white-space:nowrap}
.nav li.active{font-weight:700;color:#fff}
.nav svg{position:absolute;left:722px;top:18px}

/* logo */
.brand{left:114px;top:7px;width:96px;height:96px;border-radius:50%;background:#fff;border:3px solid var(--purple);display:flex;align-items:center;justify-content:center;text-align:center;z-index:3}
.brand span{font-family:"Roboto Condensed",sans-serif;font-weight:700;font-size:10px;line-height:1.2;color:var(--purple);padding:0 10px}

/* hero */
.hero{left:0;top:94px;width:843px;height:276px;border-bottom:4px solid var(--purple);
  background:linear-gradient(90deg,#3b2f2c 0%,#6b5046 30%,#8a6a58 50%,#a8896e 70%,#6d5648 100%)}
.hero::after{content:"";position:absolute;inset:0;background:rgba(20,15,25,.28)}
.hero h1{position:absolute;left:120px;top:98px;width:603px;text-align:center;color:#fff;font-family:"Roboto Condensed",sans-serif;font-weight:700;font-size:26px;line-height:30px;z-index:2}
.btn{top:206px;height:27px;font-family:"Roboto Condensed",sans-serif;font-weight:700;font-size:10px;color:#fff;display:flex;align-items:center;justify-content:center;z-index:2;letter-spacing:.3px}
.btn.primary{left:281px;width:153px;background:var(--purple)}
.btn.ghost{left:441px;width:121px;background:rgba(60,50,45,.75)}
.hero-arrow{left:50px;top:227px;z-index:2}

/* news strip */
.strip-item{top:400px;display:flex;gap:15px}
.thumb{width:64px;height:64px;border-radius:50%;flex:none}
.strip-item h3{font-family:"Roboto Condensed",sans-serif;font-weight:700;font-size:10px;color:var(--purple);margin-top:7px;margin-bottom:4px}
.strip-item p{font-size:7.5px;line-height:9.5px;width:110px;color:#444}
.rule{left:112px;top:495px;width:618px;height:1px;background:#e2e2e2}

/* welcome */
.welcome h2{position:absolute;left:0;top:532px;width:843px;text-align:center;font-family:"Roboto Condensed",sans-serif;font-weight:400;font-size:20px;color:var(--ink)}
.welcome p{position:absolute;left:146px;width:550px;text-align:center;font-size:7.6px;line-height:13.6px;color:#555}

/* school cards */
.school{top:727px;width:202px;height:86px;background:var(--card);display:flex;align-items:center;padding-left:14px;gap:16px}
.school .pic{width:64px;height:64px;border-radius:50%;background:#cfcfcf;flex:none}
.school h4{font-family:"Roboto Condensed",sans-serif;font-weight:700;font-size:12px;line-height:14.5px;color:#555;text-transform:uppercase}
.school.active{background:var(--purple)}
.school.active .pic{background:var(--purple-deep)}
.school.active h4{color:#fff}

/* latest news */
.band{left:0;top:857px;width:843px;height:291px;background:var(--light)}
.band-title{left:112px;top:896px;font-family:"Roboto Condensed",sans-serif;font-weight:400;font-size:20px;color:var(--ink)}
.band-rule{left:112px;top:930px;width:443px;height:1px;background:#d4d4d4}
.band-arrows{left:521px;top:903px}
.news-card{top:943px;width:148px;height:188px;padding:11px 0 0 0}
.news-card.hl{background:#e0e0e0;border-radius:4px}
.news-card .thumb{width:65px;height:65px;margin-bottom:18px}
.news-card h5{font-family:"Roboto Condensed",sans-serif;font-weight:700;font-size:10px;color:var(--ink);margin-bottom:4px}
.news-card p{font-size:7.5px;line-height:9.5px;color:#444;width:125px}
.news-card a{display:block;margin-top:12px;font-size:7.5px;font-weight:600;color:var(--ink);text-decoration:none}
.news-card.hl h5,.news-card.hl a{color:var(--purple)}

/* calendar */
.cal{left:576px;top:893px;width:153px;height:240px;background:#f4f4f4;border:1px solid #d8d8d8;border-radius:3px;overflow:hidden}
.cal-head{height:123px;background:var(--purple-soft);color:#fff;padding:12px 0 0 6px;position:relative}
.cal-head .day{font-size:9.5px;padding-left:14px}
.cal-head .month{font-size:9.5px}
.cal-head .date{font-size:40px;font-weight:400;line-height:44px;letter-spacing:-1px}
.cal-head .nav-arrows{position:absolute;right:8px;top:13px;font-size:10px;display:flex;gap:14px}
.grid{display:grid;grid-template-columns:repeat(7,21px);justify-content:center;row-gap:3px;padding-top:6px}
.grid span{height:13px;width:13px;margin:0 auto;border-radius:50%;font-size:7px;display:flex;align-items:center;justify-content:center;color:#777}
.grid .h{font-family:"Roboto Condensed",sans-serif;font-weight:700;color:var(--purple);font-size:8px;width:auto}
.grid .f{color:#ccc}
.grid .g{background:#c4c4c4;color:#fff}
.grid .d{background:var(--navy);color:#fff}
.grid .o{background:var(--gold);color:#fff}

/* footer */
.footer{left:0;top:1148px;width:843px;height:52px;background:var(--footer)}
.footer .copy{position:absolute;left:114px;top:22px;font-size:7.5px;color:#777;display:flex;align-items:center;gap:12px}
.footer .copy .dot{width:12px;height:12px;border-radius:50%;background:var(--purple)}
.footer .social{left:683px;top:22px}
.footer .social i{background:#666}
.footer .social i:first-child{background:var(--purple)}
</style>
</head>
<body>

<header>
  <div class="abs topbar"></div>
  <div class="abs visits"><span class="dot"></span><span><b>( 15200 )</b> USERS VISITED</span></div>
  <div class="abs lang"><span>ARABIC</span><span>ENGLISH</span></div>
  <div class="abs social"><i></i><i></i><i></i></div>

  <nav class="abs nav">
    <ul>
      <li class="active" style="left:242px">HOME</li>
      <li style="left:289px">ABOUT US</li>
      <li style="left:354px">SCHOOLS</li>
      <li style="left:414px">EVENTS</li>
      <li style="left:468px">STUDENTS</li>
      <li style="left:532px">GALLERY</li>
      <li style="left:591px">LECTURES</li>
      <li style="left:653px">CONTACT US</li>
    </ul>
    <svg width="9" height="9" viewBox="0 0 9 9"><circle cx="3.7" cy="3.7" r="2.8" fill="none" stroke="#fff" stroke-width="1.2"/><line x1="5.8" y1="5.8" x2="8.5" y2="8.5" stroke="#fff" stroke-width="1.2"/></svg>
  </nav>

  <div class="abs brand"><span>Bayt Qamarin Private Schools</span></div>
</header>

<section class="abs hero" role="img" aria-label="Photo of smiling graduates in caps and gowns celebrating">
  <h1>LOREM IPSUM DOLOR SIT AMET, CONSECTETUER ADIPISCING ELIT</h1>
  <div class="abs btn primary">GET STARTED NOW</div>
  <div class="abs btn ghost">ABOUT US</div>
</section>
<svg class="abs hero-arrow" width="14" height="10" viewBox="0 0 14 10" style="z-index:2"><path d="M13 5H2M5 1.5 1.5 5 5 8.5" fill="none" stroke="#8f62c0" stroke-width="1.3"/></svg>

<section>
  <div class="abs strip-item" style="left:113px">
    <div class="thumb" role="img" aria-label="Photo of a young schoolgirl" style="background:#d9c2a8"></div>
    <div><h3>LATEST NEWS</h3><p>Lorem ipsum dolor sit amet, consectetuer adipiscing elit, sed diam dolore magna aliquam erat volutpat.</p></div>
  </div>
  <div class="abs strip-item" style="left:321px">
    <div class="thumb" role="img" aria-label="Photo of a toddler in a graduation cap with an abacus" style="background:#8d73b8"></div>
    <div><h3>LATEST NEWS 2</h3><p>Ut wisi enim ad minim veniam, quis nostrud exerci tation ullamcorper suscipit lobortis nisl ut aliquip consequat.</p></div>
  </div>
  <div class="abs strip-item" style="left:529px">
    <div class="thumb" role="img" aria-label="Photo of library bookshelves" style="background:#8a5a33"></div>
    <div><h3>LATEST NEWS 3</h3><p>Duis autem vel eum iriure dolor in hendrerit in vulputate velit esse facilisi.</p></div>
  </div>
  <div class="abs rule"></div>
</section>

<section class="welcome">
  <h2>WELCOME</h2>
  <p style="top:566px">Lorem ipsum dolor sit amet, consectetuer adipiscing elit, sed diam nonummy nibh euismod tincidunt ut laoreet dolore magna aliquam erat volutpat. Ut wisi enim ad minim veniam, quis nostrud exerci tation ullamcorper suscipit lobortis nisl ut aliquip ex ea commodo consequat. Duis autem vel eum iriure dolor in hendrerit in vulputate velit esse molestie consequat, vel illum dolore eu feugiat nulla facilisis at vero eros et accumsan et iusto odio dignissim qui blandit praesent luptatum zzril delenit augue duis dolore te feugait nulla facilisi.</p>
  <p style="top:631px">Duis autem vel eum iriure dolor in hendrerit in vulputate velit esse molestie consequat, vel illum dolore eu feugiat nulla facilisis at vero eros et accumsan et iusto odio dignissim qui blandit praesent luptatum zzril delenit augue duis dolore te feugait nulla facilisi. Lorem ipsum dolor sit amet, consectetuer adipiscing elit, sed diam nonummy nibh euismod tincidunt ut laoreet dolore magna aliquam erat volutpat.</p>
  <p style="top:686px">Ut wisi enim ad minim veniam, quis nostrud exerci tation ullamcorper suscipit lobortis nisl ut aliquip ex ea commodo consequat.</p>
</section>

<section>
  <div class="abs school" style="left:113px"><div class="pic" role="img" aria-label="Illustration of a little girl with a teddy bear"></div><h4>Bayt Qamarin Primary School</h4></div>
  <div class="abs school active" style="left:320px"><div class="pic" role="img" aria-label="Illustration of a girl in a graduation cap"></div><h4>Bayt Qamarin High School for Girls</h4></div>
  <div class="abs school" style="left:527px"><div class="pic" role="img" aria-label="Illustration of a boy in a graduation cap"></div><h4>Bayt Qamarin High School for Boys</h4></div>
</section>

<section>
  <div class="abs band"></div>
  <h2 class="abs band-title">LATEST NEWS</h2>
  <svg class="abs band-arrows" width="34" height="12" viewBox="0 0 34 12"><path d="M13 6H1M5 2 1 6 5 10" fill="none" stroke="#999" stroke-width="1.3"/><path d="M20 6H33M29 2 33 6 29 10" fill="none" stroke="#6d44a5" stroke-width="1.3"/></svg>
  <div class="abs band-rule"></div>

  <article class="abs news-card" style="left:113px">
    <div class="thumb" role="img" aria-label="Photo of library bookshelves" style="background:#8a5a33"></div>
    <h5>LATEST NEWS</h5><p>Lorem ipsum dolor sit amet, consectetuer adipiscing elit, sed diam dolore magna aliquam erat volutpat.</p><a>Read More</a>
  </article>
  <article class="abs news-card hl" style="left:250px;padding-left:13px">
    <div class="thumb" role="img" aria-label="Photo of a young schoolgirl" style="background:#b08fc8"></div>
    <h5>LATEST NEWS</h5><p>Lorem ipsum dolor sit amet, consectetuer adipiscing elit, sed diam dolore magna aliquam erat volutpat.</p><a>Read More</a>
  </article>
  <article class="abs news-card" style="left:420px">
    <div class="thumb" role="img" aria-label="Photo of a toddler in a graduation cap with an abacus" style="background:#c9d3e6"></div>
    <h5>LATEST NEWS</h5><p>Lorem ipsum dolor sit amet, consectetuer adipiscing elit, sed diam dolore magna aliquam erat volutpat.</p><a>Read More</a>
  </article>

  <aside class="abs cal">
    <div class="cal-head">
      <div class="day">Friday</div>
      <div class="month">March 2014</div>
      <div class="date">28</div>
      <div class="nav-arrows"><span>&#8249;</span><span>&#8250;</span></div>
    </div>
    <div class="grid">
      <span class="h">M</span><span class="h">T</span><span class="h">W</span><span class="h">T</span><span class="h">F</span><span class="h">S</span><span class="h">S</span>
      <span class="f">24</span><span class="f">25</span><span class="g">26</span><span class="f">27</span><span class="f">28</span><span>1</span><span>2</span>
      <span>3</span><span>4</span><span>5</span><span class="d">6</span><span>7</span><span class="d">8</span><span class="d">9</span>
      <span>10</span><span>11</span><span class="d">12</span><span>13</span><span>14</span><span>15</span><span>16</span>
      <span>17</span><span class="d">18</span><span>19</span><span>20</span><span>21</span><span class="d">22</span><span class="d">23</span>
      <span>24</span><span>25</span><span class="d">26</span><span>27</span><span class="o">28</span><span>29</span><span>30</span>
      <span>31</span><span class="f">1</span><span class="f">2</span><span class="f">3</span><span class="f">4</span><span class="f">5</span><span class="f">6</span>
    </div>
  </aside>
</section>

<footer class="abs footer">
  <div class="copy"><span>© 2015 ALL RIGHTS RESERVED.</span><span class="dot"></span><span>( 15200 ) USERS VISITED</span></div>
  <div class="abs social"><i></i><i></i><i></i></div>
</footer>

</body>
</html>
```